Business Card and stationery
Use same font as used in my logo
Delia Frost
4127 E Copper Ln
Scottsdale, Az 85299
delia@thewillowparlorshop.com
www.thewillowparlorshop.com
Store Hours
Wed & Fri 11am - 3 pm
And By Appointment

```html
<!DOCTYPE html>
<html lang="en">
<head>
<meta charset="utf-8">
<title>Larkspur Boutique – Business Cards</title>
<link href="https://fonts.googleapis.com/css2?family=Open+Sans:wght@400;700&display=swap" rel="stylesheet">
<style>
  :root {
    --bg: #ece8e2;
    --ink: #0d0d0d;
    --paper: #ffffff;
    --text-light: #ffffff;
    --text-dark: #111111;
  }
  html, body {
    margin: 0;
    padding: 0;
    width: 1200px;
    height: 852px;
    overflow: hidden;
    background: var(--bg);
    font-family: "Open Sans", Arial, sans-serif;
  }
  .canvas {
    position: relative;
    width: 1200px;
    height: 852px;
  }
  .card {
    position: absolute;
    width: 560px;
    height: 320px;
    border-radius: 18px;
    overflow: hidden;
    display: flex;
    box-shadow: 0 4px 14px rgba(0,0,0,0.18);
  }
  .card--left-info { left: 100px; top: 110px; }
  .card--right-info { left: 540px; top: 420px; }

  .info-panel {
    width: 250px;
    background: var(--ink);
    color: var(--text-light);
    box-sizing: border-box;
    padding: 34px 22px 26px;
    display: flex;
    flex-direction: column;
    font-size: 13px;
    line-height: 1.45;
  }
  .card--right-info .info-panel {
    text-align: right;
    align-items: flex-end;
  }
  .brand-panel {
    flex: 1;
    background: var(--paper);
    display: flex;
    align-items: center;
    justify-content: center;
  }
  .name {
    font-weight: 700;
    font-size: 17px;
    margin: 0 0 64px;
  }
  .address { margin: 0 0 22px; }
  .contacts {
    list-style: none;
    margin: 0;
    padding: 0;
  }
  .contacts li {
    display: flex;
    align-items: center;
    gap: 8px;
    height: 19px;
  }
  .card--right-info .contacts li { flex-direction: row-reverse; }
  .icon { width: 11px; height: 11px; flex: none; }

  .wordmark {
    display: flex;
    align-items: center;
    gap: 12px;
    color: var(--text-dark);
    font-weight: 700;
    font-size: 22px;
    letter-spacing: 0.5px;
  }
  .wordmark-square {
    width: 16px;
    height: 16px;
    background: var(--text-dark);
  }
</style>
</head>
<body>
<div class="canvas">

  <article class="card card--left-info">
    <section class="info-panel">
      <p class="name">Delia Frost</p>
      <p class="address">4127 E Copper Ln<br>Scottsdale, Az 85299</p>
      <ul class="contacts">
        <li><svg class="icon" viewBox="0 0 12 12"><rect x="3" y="0.5" width="6" height="11" rx="1.2" fill="#fff"/></svg>(480) 555-0142</li>
        <li><svg class="icon" viewBox="0 0 12 12"><path d="M2 1h3l1 3-2 1.2a7 7 0 0 0 2.8 2.8L8 6l3 1v3a1 1 0 0 1-1 1A9 9 0 0 1 1 2a1 1 0 0 1 1-1z" fill="#fff"/></svg>480-555-0187</li>
        <li><svg class="icon" viewBox="0 0 12 12"><rect x="0.5" y="2" width="11" height="8" fill="#fff"/><path d="M0.5 2l5.5 4.5L11.5 2" stroke="#0d0d0d" fill="none"/></svg>delia@thewillowparlorshop.com</li>
        <li><svg class="icon" viewBox="0 0 12 12"><circle cx="6" cy="6" r="5.5" fill="#fff"/></svg>www.thewillowparlorshop.com</li>
      </ul>
    </section>
    <section class="brand-panel">
      <div class="wordmark"><span class="wordmark-square"></span>The Larkspur Boutique</div>
    </section>
  </article>

  <article class="card card--right-info">
    <section class="brand-panel">
      <div class="wordmark"><span class="wordmark-square"></span>The Larkspur Boutique</div>
    </section>
    <section class="info-panel">
      <p class="name">Delia Frost</p>
      <p class="address">4127 E Copper Ln<br>Scottsdale, Az 85299</p>
      <ul class="contacts">
        <li><svg class="icon" viewBox="0 0 12 12"><rect x="3" y="0.5" width="6" height="11" rx="1.2" fill="#fff"/></svg>(480) 555-0142</li>
        <li><svg class="icon" viewBox="0 0 12 12"><path d="M2 1h3l1 3-2 1.2a7 7 0 0 0 2.8 2.8L8 6l3 1v3a1 1 0 0 1-1 1A9 9 0 0 1 1 2a1 1 0 0 1 1-1z" fill="#fff"/></svg>480-555-0187</li>
        <li><svg class="icon" viewBox="0 0 12 12"><rect x="0.5" y="2" width="11" height="8" fill="#fff"/><path d="M0.5 2l5.5 4.5L11.5 2" stroke="#0d0d0d" fill="none"/></svg>delia@thewillowparlorshop.com</li>
        <li><svg class="icon" viewBox="0 0 12 12"><circle cx="6" cy="6" r="5.5" fill="#fff"/></svg>www.thewillowparlorshop.com</li>
      </ul>
    </section>
  </article>

</div>
</body>
</html>
```